Packaging Tape Design for Retail / Ecommerce Company

We need a design for custom packing tape for our company. We would like to see two designs for the packaging tape. 1) with the word fragile attached 2) Similiar design without the fragileMinimum resolution is 300 .ppi 3" x 6" or 3" x 12" - If selected, request that font that are used be identified. Orla Hearth Logo and package - Nest Bright! is a tagline we use on documents and correspondence. Looking for a creative design.

Target Market(s)

Mid level to high end consumers

Industry/Entity Type

Retail

Font styles to use
Sans Serif

Requirements
Must have
• logo must be included
• Nest Bright! - must be included
• web address: orlahearth.com
Nice to have
• creativity

```html
<!DOCTYPE html>
<html lang="en">
<head>
<meta charset="utf-8">
<title>Orla Hearth – Packing Tape Set</title>
<link rel="stylesheet" href="https://fonts.googleapis.com/css2?family=Roboto:wght@400;700&display=swap">
<style>
  :root {
    --stage: #6a6a6a;
    --tape: #ffffff;
    --brand-red: #a32a27;
    --strip-red: #8f2420;
    --cream: #efe6cc;
  }
  html, body {
    margin: 0;
    padding: 0;
    width: 1200px;
    height: 952px;
    overflow: hidden;
    background: var(--stage);
  }
  .canvas {
    position: relative;
    width: 1200px;
    height: 952px;
    background: radial-gradient(ellipse at center, #b9b9b9 0%, #7a7a7a 55%, #555 100%);
  }
  .tape {
    position: absolute;
    left: 50px;
    width: 1100px;
    height: 300px;
    box-shadow: 0 10px 30px rgba(0,0,0,0.25);
  }
  .tape--fragile { top: 150px; }
  .tape--plain { top: 502px; }
  .tape svg { display: block; }
  .web-address {
    font-family: "Roboto", Arial, sans-serif;
    font-weight: 700;
    font-size: 17px;
    fill: var(--brand-red);
  }
  .brand-name {
    font-family: "Roboto", Arial, sans-serif;
    font-weight: 700;
    font-size: 26px;
    fill: var(--brand-red);
    letter-spacing: 1px;
  }
  .fragile-label {
    font-family: "Roboto", Arial, sans-serif;
    font-weight: 700;
    font-size: 11px;
    fill: var(--brand-red);
    letter-spacing: 1px;
  }
  .tagline {
    font-family: "Roboto", Arial, sans-serif;
    font-weight: 700;
    font-size: 22px;
    fill: var(--brand-red);
  }
</style>
</head>
<body>
<main class="canvas">
  <svg width="0" height="0" style="position:absolute" aria-hidden="true">
    <defs>
      <linearGradient id="dotTone" x1="0" y1="0" x2="0" y2="1">
        <stop offset="0" stop-color="#ffffff"/>
        <stop offset="0.5" stop-color="#eeeeee"/>
        <stop offset="1" stop-color="#ffffff"/>
      </linearGradient>
      <g id="start-strip">
        <rect x="0" y="0" width="60" height="300" fill="var(--strip-red)"/>
        <g fill="#ffffff">
          <path d="M22 62 h10 v-7 l12 12 l-12 12 v-7 h-10 z"/>
          <path d="M22 104 h10 v-7 l12 12 l-12 12 v-7 h-10 z"/>
          <path d="M22 146 h10 v-7 l12 12 l-12 12 v-7 h-10 z"/>
          <path d="M22 188 h10 v-7 l12 12 l-12 12 v-7 h-10 z"/>
          <path d="M22 230 h10 v-7 l12 12 l-12 12 v-7 h-10 z"/>
        </g>
      </g>
      <g id="brand-band">
        <rect x="-32" y="0" width="64" height="300" fill="var(--cream)"/>
        <rect x="-32" y="0" width="15" height="300" fill="var(--brand-red)"/>
        <rect x="17" y="0" width="15" height="300" fill="var(--brand-red)"/>
        <rect x="-52" y="68" width="104" height="164" rx="14" fill="var(--cream)" stroke="#ffffff" stroke-width="3"/>
        <text class="brand-name" transform="translate(9,150) rotate(-90)" text-anchor="middle">Orla Hearth</text>
      </g>
      <g id="fragile-mark">
        <circle r="40" fill="var(--brand-red)"/>
        <circle r="31" fill="var(--cream)"/>
        <text class="fragile-label" transform="rotate(-90)" text-anchor="middle" y="4">FRAGILE</text>
      </g>
      <g id="addresses">
        <text class="web-address" x="342" y="288" text-anchor="middle">orlahearth.com</text>
        <text class="web-address" x="687" y="288" text-anchor="middle">orlahearth.com</text>
        <text class="web-address" x="1032" y="288" text-anchor="middle">orlahearth.com</text>
        <text class="web-address" transform="translate(342,12) rotate(180)" text-anchor="middle">orlahearth.com</text>
        <text class="web-address" transform="translate(687,12) rotate(180)" text-anchor="middle">orlahearth.com</text>
        <text class="web-address" transform="translate(1032,12) rotate(180)" text-anchor="middle">orlahearth.com</text>
      </g>
    </defs>
  </svg>

  <section class="tape tape--fragile" aria-label="Orla Hearth packing tape with fragile mark">
    <svg width="1100" height="300" viewBox="0 0 1100 300" xmlns="http://www.w3.org/2000/svg">
      <rect width="1100" height="300" fill="var(--tape)"/>
      <rect role="img" aria-label="Soft grey halftone dot pattern" x="60" y="30" width="1040" height="240" fill="url(#dotTone)"/>
      <use href="#start-strip"/>
      <use href="#brand-band" x="170"/>
      <use href="#brand-band" x="515"/>
      <use href="#brand-band" x="860"/>
      <use href="#fragile-mark" x="342" y="150"/>
      <use href="#fragile-mark" x="687" y="150"/>
      <use href="#fragile-mark" x="1032" y="150"/>
      <use href="#addresses"/>
    </svg>
  </section>

  <section class="tape tape--plain" aria-label="Orla Hearth packing tape with tagline">
    <svg width="1100" height="300" viewBox="0 0 1100 300" xmlns="http://www.w3.org/2000/svg">
      <rect width="1100" height="300" fill="var(--tape)"/>
      <rect role="img" aria-label="Soft grey halftone dot pattern" x="60" y="30" width="1040" height="240" fill="url(#dotTone)"/>
      <use href="#start-strip"/>
      <use href="#brand-band" x="170"/>
      <use href="#brand-band" x="515"/>
      <use href="#brand-band" x="860"/>
      <text class="tagline" x="342" y="158" text-anchor="middle">Nest Bright!</text>
      <text class="tagline" x="687" y="158" text-anchor="middle">Nest Bright!</text>
      <text class="tagline" x="1032" y="158" text-anchor="middle">Nest Bright!</text>
      <use href="#addresses"/>
    </svg>
  </section>
</main>
</body>
</html>
```